Banner dimension 1767 X 887 for Tolvenko website

Need one banner for our website www.tolvenko.com.au, The dimension of the banner should be 1767 x 887. Attached to this brief are two images that needs to be on that one banner, PLEASE DO NOT SEND SEPARATE BANNERS, both images on the same banner. Thanks

The banner should have the following message on it:

1.) " Take a further 40% off all stock" ( use code: TOLVENKO. Ends 31/12/2015)
2.) " Kick back or kick it up a notch this Autumn in the most versatile pique striped polo shirts and Pinafore belt strap denim dress"

Target Market(s)

kids aged 5-12yrs

Requirements
Must have
• very playful

```html
<!DOCTYPE html>
<html lang="en">
<head>
<meta charset="utf-8">
<title>Tolvenko – Take a further 40% off all stock</title>
<link rel="stylesheet" href="https://fonts.googleapis.com/css2?family=Oswald:wght@500&family=Saira+Stencil+One&family=Antonio:wght@400;600&display=swap">
<style>
  :root {
    --ink: #111111;
    --magenta: #e0157f;
    --panel-blue: #9fd5f2;
    --panel-blue-deep: #82c7ec;
    --panel-lilac: #b8c6ee;
    --wash-lilac: #d8d0ea;
    --wash-blue: #c6e2f2;
    --wash-white: #f3f1f6;
    --strip-blue: #5fb6e3;
    --band-black: #1c1d21;
    --band-text: #ffffff;
  }
  * { box-sizing: border-box; margin: 0; padding: 0; }
  html, body { width: 1200px; height: 602px; overflow: hidden; background: #ffffff; }
  .banner { position: relative; width: 1200px; height: 602px; overflow: hidden; }

  .backdrop-wash {
    position: absolute; inset: 0;
    background:
      radial-gradient(ellipse at 12% 35%, var(--wash-blue) 0%, transparent 45%),
      radial-gradient(ellipse at 88% 45%, var(--wash-lilac) 0%, transparent 50%),
      radial-gradient(ellipse at 55% 85%, var(--wash-lilac) 0%, transparent 45%),
      linear-gradient(135deg, var(--wash-white), #e4e1ee 50%, var(--wash-white));
  }
  .floor-strip {
    position: absolute; left: 0; right: 0; bottom: 0; height: 40px;
    background: var(--strip-blue);
  }
  .offer-panel {
    position: absolute; left: 305px; top: 30px; width: 517px; height: 412px;
    background: linear-gradient(165deg, var(--panel-blue) 0%, var(--panel-blue-deep) 55%, var(--panel-lilac) 100%);
  }

  .kid-photo { position: absolute; border-radius: 45% 45% 10% 10% / 14% 14% 6% 6%; opacity: .85; }
  .kid-photo--girl {
    left: 66px; top: 25px; width: 232px; height: 552px;
    background: linear-gradient(180deg, #6a4a3a 0%, #f2f2f2 22%, #4d7191 40%, #6f8da8 68%, #e9c9b5 82%, #e27a9b 100%);
  }
  .kid-photo--boy {
    left: 832px; top: 62px; width: 288px; height: 508px;
    background: linear-gradient(180deg, #4a3426 0%, #3b6b4c 28%, #8aa3bd 58%, #d9b59c 80%, #2a2a2a 100%);
  }

  .offer-line {
    position: absolute; left: 305px; width: 517px;
    text-align: center; white-space: nowrap; color: var(--ink);
  }
  .offer-lead {
    top: 50px;
    font-family: "Antonio", sans-serif; font-weight: 600;
    font-size: 56px; line-height: 60px; letter-spacing: 1px;
  }
  .offer-figure {
    position: absolute; left: 404px; top: 96px; width: 205px;
    text-align: center; color: var(--magenta);
    font-family: "Saira Stencil One", sans-serif;
    font-size: 188px; line-height: 170px; letter-spacing: -6px;
    transform: scaleX(0.86); transform-origin: left center;
  }
  .offer-percent {
    position: absolute; left: 630px; top: 108px; width: 90px;
    text-align: center; color: var(--magenta);
    font-family: "Saira Stencil One", sans-serif;
    font-size: 78px; line-height: 80px;
  }
  .offer-off {
    position: absolute; left: 612px; top: 180px; width: 104px;
    text-align: center; color: var(--magenta);
    font-family: "Saira Stencil One", sans-serif;
    font-size: 56px; line-height: 70px;
    transform: scaleX(0.82); transform-origin: center;
  }
  .offer-scope {
    top: 252px;
    font-family: "Saira Stencil One", sans-serif;
    font-size: 64px; line-height: 64px;
    transform: scaleX(0.86); transform-origin: center;
  }
  .offer-code {
    top: 318px;
    font-family: "Antonio", sans-serif; font-weight: 400;
    font-size: 44px; line-height: 46px; color: var(--magenta); letter-spacing: 1px;
  }
  .offer-expiry {
    top: 360px;
    font-family: "Antonio", sans-serif; font-weight: 400;
    font-size: 52px; line-height: 54px; letter-spacing: 1px;
  }

  .tagline-band {
    position: absolute;
    background: var(--band-black); color: var(--band-text);
    font-family: "Oswald", sans-serif; font-weight: 500;
    text-transform: uppercase; white-space: nowrap;
    display: flex; align-items: center; justify-content: center;
  }
  .tagline-band--lead {
    left: 330px; top: 424px; width: 490px; height: 60px;
    font-size: 27px; letter-spacing: 3.5px; transform: rotate(1.6deg);
  }
  .tagline-band--middle {
    left: 368px; top: 486px; width: 530px; height: 38px;
    font-size: 18px; letter-spacing: 2.6px; transform: rotate(1.2deg);
  }
  .tagline-band--last {
    left: 312px; top: 527px; width: 546px; height: 38px;
    font-size: 18px; letter-spacing: 2.8px; transform: rotate(1deg);
  }
</style>
</head>
<body>
  <main class="banner">
    <div class="backdrop-wash" role="img" aria-label="Soft blue and lilac watercolour wash background"></div>
    <div class="floor-strip"></div>

    <div class="offer-panel"></div>

    <div class="kid-photo kid-photo--girl" role="img" aria-label="Photo of a smiling girl in a white tee, pinafore belt strap denim dress and pink sneakers"></div>
    <div class="kid-photo kid-photo--boy" role="img" aria-label="Photo of a playful boy in a green striped pique polo shirt and denim cargo shorts"></div>

    <section class="offer-copy" aria-label="Offer">
      <p class="offer-line offer-lead">TAKE A FURTHER</p>
      <p class="offer-figure">40</p>
      <p class="offer-percent">%</p>
      <p class="offer-off">OFF</p>
      <p class="offer-line offer-scope">ALL STOCK</p>
      <p class="offer-line offer-code">use code: TOLVENKO</p>
      <p class="offer-line offer-expiry">ends 31/12/2015</p>
    </section>

    <p class="tagline-band tagline-band--lead">Kick back or kick it up a notch</p>
    <p class="tagline-band tagline-band--middle">This autumn in the most versatile pique striped</p>
    <p class="tagline-band tagline-band--last">Polo shirts and pinafore belt strap denim dress</p>
  </main>
</body>
</html>
```